WP website design (Vorne)

We need a wordpress design for an established auction and real estate company based in Kentucky. The winning design will incorporate a professional color scheme with company logo in a clean layout with specified widgets. The design needs to consider that this will be developed on a responsive theme. Colors will complement the colors in the logo.

Industry/Entity Type

Real Estate

Font styles to use
Sans Serif

Requirements
Must have
• - Navigation:
1) Home 2) Auctions 3) Real Estate Listings 4) Our Services 5) Why Auctions 6) About Us 7) Past Auctions 8) Contact Us

Homeage will have slideshow, please use stock real estate image as the initial slide. Homepage will have this content: "Martin Vorne Auctioneer Real Estate Broker

Buying or selling you can count on Martin Vorne Auctioneer to deliver a quality auction experience. We handle all the details from initial handshake to final payment. We are with you every step of the way giving our sellers the service and results they deserve. You only have one chance for a successful auction. Contact us today to see how our experience and know-how can work for you. We are confident that you will appreciate our higher standard of service."

Footer will have smaller company logo, and attached association logos and this contact info:
Phone: (270) 555-0148
Contacts: Martin Vorne
Email: martinvorne@mailbrook.example
Address: 482 Pellworth Lane • Bowling Green, KY 42917

Widgets:
1) email sign up 2) Social media (twitter, Youtube - can also be in header 3) News & Events Blog widget 4) testimonials blog 5) Featured Video widget
Nice to have
• Nice to Have:
- demonstrate the drop-down menu styling, e.g. under Auctions
-Upcoming Auctions
-Online Auctions
-Past Auctions

```html
<!DOCTYPE html>
<html lang="en">
<head>
<meta charset="utf-8">
<title>Martin Vorne Auctioneer Real Estate Broker</title>
<link href="https://fonts.googleapis.com/css2?family=Arvo:wght@400;700&family=PT+Sans:wght@400;700&display=swap" rel="stylesheet">
<style>
:root{
  --blue:#2a5ba8;
  --blue-dark:#1f4b91;
  --blue-nav:#2c5ea9;
  --yellow:#e9b412;
  --yellow-light:#f2c83a;
  --text:#7d7d7d;
  --text-dark:#555;
  --head:#2d5da6;
  --page:#fbfbfb;
  --band:#ececec;
  --footer:#e4e4e4;
}
*{margin:0;padding:0;box-sizing:border-box}
html,body{width:955px;height:1200px;overflow:hidden}
body{background:var(--page);font-family:"PT Sans",Arial,sans-serif;color:var(--text);position:relative}
.abs{position:absolute}

.site-header{left:0;top:0;width:955px;height:103px;background:var(--blue)}
.brand{left:127px;top:0;width:95px;height:96px;background:#fff;border-radius:0 0 6px 6px;display:flex;flex-direction:column;align-items:center;justify-content:center;gap:6px}
.brand-mark{width:18px;height:18px;background:var(--blue)}
.brand-name{font-family:"PT Sans",sans-serif;font-weight:700;font-size:13px;color:var(--blue);text-align:center;line-height:1.1}
.social{display:flex;gap:9px}
.social span{display:block;width:25px;height:25px;border-radius:3px}
.header-social{left:701px;top:21px}
.s1{background:#3b5a9a}.s2{background:#2fa8e0}.s3{background:#1f73a8}.s4{background:#d23a2c}
.call{right:124px;top:62px;font-size:20px;color:#9fb6dc;display:flex;align-items:center;gap:5px}
.call b{color:var(--yellow);font-weight:400}

.main-nav{left:0;top:103px;width:955px;height:36px;background:var(--blue-nav);border-top:1px solid #3c6db5;border-bottom:1px solid #1e4685}
.main-nav ul{list-style:none;display:flex;margin-left:128px;height:100%;border-left:1px solid #214f93}
.main-nav li{padding:0 19px;line-height:35px;font-size:11px;font-weight:700;color:#fff;border-right:1px solid #214f93}
.main-nav li.active{background:#224f95}
.dropdown{left:196px;top:139px;width:133px;height:75px;background:var(--blue);box-shadow:0 2px 4px rgba(0,0,0,.3);padding:8px 0 0 12px;list-style:none}
.dropdown li{font-size:10px;color:#fff;line-height:21px}
.dropdown li::before{content:"›";margin-right:5px}

.hero{left:0;top:139px;width:955px;height:333px;background:linear-gradient(180deg,#c9d4dc 0%,#9aa4a8 35%,#7a4a3a 55%,#5d4030 72%,#6f8a45 85%,#6b8840 100%);z-index:-1}
.hero-title{left:127px;top:268px;width:403px;height:86px;background:rgba(33,82,160,.85);padding:14px 0 0 28px}
.hero-title h1{font-family:"Arvo",serif;font-weight:400;font-size:28px;color:#fff;line-height:1.1}
.hero-title p{font-family:"Arvo",serif;font-size:13px;color:var(--yellow);letter-spacing:1px;margin-top:4px;text-transform:uppercase}

.intro h2{font-family:"Arvo",serif;font-weight:400;font-size:18px;color:var(--head)}
.intro{left:128px;top:496px;width:345px}
.intro p{font-size:10.3px;line-height:15px;margin-top:12px}
.intro p+p{margin-top:15px}
.video{left:488px;top:499px;width:344px;height:171px;border-radius:3px;overflow:hidden;background:linear-gradient(180deg,#9bbbd8 0%,#b7a58b 40%,#8a7a60 70%,#4f6a34 100%)}
.video-bar{left:0;bottom:0;width:344px;height:29px;background:rgba(20,20,20,.8)}
.divider{left:128px;top:699px;width:700px;height:3px;border-top:1px dotted #c8c8c8;border-bottom:1px dotted #c8c8c8}

.col-title{font-family:"Arvo",serif;font-weight:400;font-size:14px;color:var(--head)}
.testimonial{left:128px;top:731px;width:188px}
.client{display:flex;gap:10px;margin-top:18px;align-items:center}
.avatar{width:38px;height:38px;background:linear-gradient(#c9a98c,#8a6a50)}
.client b{display:block;font-weight:400;font-size:13px;color:var(--text-dark)}
.client small{font-size:9.5px;color:#aaa}
.quote{margin-top:19px;background:var(--blue);color:#fff;font-size:10.5px;line-height:18px;padding:13px 14px 13px 31px;position:relative;height:81px}
.quote::before{content:"";position:absolute;left:13px;top:-8px;border:5px solid transparent;border-bottom:4px solid var(--blue);border-left-color:var(--blue)}
.quote::after{content:"“";position:absolute;left:11px;top:7px;font-family:"Arvo",serif;font-size:26px;line-height:26px}

.news{left:369px;top:731px;width:220px}
.news-item{display:flex;gap:15px;margin-top:15px}
.news-item:first-of-type{margin-top:18px}
.thumb{width:40px;height:40px;flex:none}
.news-item p{font-size:8.8px;line-height:15px;color:#9aa3b1}
.news-item time{display:block;font-size:8px;color:var(--text-dark)}

.newsletter{left:604px;top:731px;width:225px;height:180px;background:#ebebeb;border:1px solid #ddd;padding:16px 20px}
.newsletter input{margin-top:15px;width:190px;height:28px;border:1px solid #d6d6d6;background:#fff;padding-left:12px;font-family:inherit;font-size:10px;color:#999}
.check{display:flex;gap:7px;margin-top:10px;font-size:10px;line-height:15px;color:#777}
.box{width:19px;height:19px;flex:none;background:var(--blue);border-radius:2px;display:flex;align-items:center;justify-content:center}
.subscribe{margin-top:12px;width:190px;height:31px;background:linear-gradient(var(--yellow-light),var(--yellow));border-radius:3px;color:#fff;font-family:"Arvo",serif;font-weight:700;font-size:10px;text-align:center;line-height:31px;letter-spacing:.3px;border-bottom:1px solid #c89a0a}

.partners{left:0;top:938px;width:955px;height:91px;background:var(--band);border-bottom:1px solid #d4d4d4}
.badge{top:16px;height:60px;background:#bdbdbd}

.site-footer{left:0;top:1030px;width:955px;height:136px;background:var(--footer)}
.footer-brand{left:133px;top:22px;width:97px;height:86px;background:#fff;border-radius:4px;display:flex;flex-direction:column;align-items:center;justify-content:center;gap:6px}
.fcol{top:23px}
.fcol h4{font-weight:400;font-size:11px;color:#666;margin-bottom:8px}
.fcol ul{list-style:none}
.fcol li{font-size:8px;line-height:18px;color:#888}
.fcol li::before{content:"";display:inline-block;border:3px solid transparent;border-left:4px solid #888;margin-right:6px}
.fcol li.on{color:#d08a0e}
.contact li::before{display:none}
.contact li{display:flex;align-items:flex-start;gap:10px;line-height:22px}
.contact svg{margin-top:6px;flex:none}
.footer-social{left:687px;top:48px;gap:9px}
.bottom{left:0;top:1166px;width:955px;height:34px;background:var(--blue);color:#fff;font-size:8px;line-height:34px}
.bottom .copy{left:130px}
.bottom .links{right:124px}
</style>
</head>
<body>

<header class="site-header abs">
  <div class="brand abs"><span class="brand-mark"></span><span class="brand-name">Martin Vorne</span></div>
  <div class="social header-social abs" aria-label="Social links"><span class="s1"></span><span class="s2"></span><span class="s3"></span><span class="s4"></span></div>
  <div class="call abs">
    <svg width="16" height="16" viewBox="0 0 24 24"><path d="M6.6 10.8a15 15 0 0 0 6.6 6.6l2.2-2.2c.3-.3.7-.4 1-.2 1.1.4 2.3.6 3.6.6.6 0 1 .4 1 1V20c0 .6-.4 1-1 1A17 17 0 0 1 3 4c0-.6.4-1 1-1h3.5c.6 0 1 .4 1 1 0 1.3.2 2.5.6 3.6.1.3 0 .7-.2 1z" fill="#9fb6dc"/></svg>
    Call us: <b>1800 555 01 48</b>
  </div>
</header>

<nav class="main-nav abs">
  <ul><li>Home</li><li class="active">Auctions</li><li>Real Estate Listings</li><li>Buyers</li><li>Sellers</li><li>Brokers</li><li>About</li><li>Contact</li></ul>
</nav>

<div class="hero abs" role="img" aria-label="Photo of a large brick house on a lawn with an auction sign in front"></div>
<ul class="dropdown abs"><li>Upcoming Auctions</li><li>Online Auctions</li><li>Past Auctions</li></ul>
<div class="hero-title abs"><h1>Martin Vorne</h1><p>Auctioneer Real Estate Broker</p></div>

<section class="intro abs">
  <h2>Martin Vorne Auctioneer Real Estate Broker</h2>
  <p>Buying or selling you can count on Martin Vorne Auctioneer to deliver a quality auction experience. We handle all the details from initial handshake to final payment. We are with you every step of the way giving our sellers the service and results they deserve. You only have one chance for a successful auction.</p>
  <p>Contact us today to see how our experience and know-how can work for you. We are confident that you will appreciate our higher standard of service.</p>
</section>

<div class="video abs" role="img" aria-label="Featured video still of a suburban house">
  <svg class="abs" style="left:147px;top:53px" width="50" height="50" viewBox="0 0 50 50"><circle cx="25" cy="25" r="22" fill="none" stroke="#fff" stroke-width="4"/><path d="M20 16l13 9-13 9z" fill="#fff"/></svg>
  <div class="video-bar abs">
    <svg width="344" height="29" viewBox="0 0 344 29">
      <circle cx="23" cy="16" r="6" fill="none" stroke="#fff" stroke-width="1.3"/><path d="M21 13l5 3-5 3z" fill="#fff"/>
      <path d="M41 13h3l4-3v12l-4-3h-3z" fill="#fff"/>
      <g fill="#fff"><rect x="56" y="12" width="1.5" height="8"/><rect x="59" y="12" width="1.5" height="8"/><rect x="62" y="12" width="1.5" height="8"/><rect x="65" y="12" width="1.5" height="8"/><rect x="68" y="12" width="1.5" height="8"/></g>
      <rect x="92" y="15" width="150" height="2" fill="#666"/><rect x="92" y="14.5" width="53" height="3" fill="#e9b412"/>
      <text x="252" y="19" font-size="7.5" fill="#fff" font-family="PT Sans,sans-serif">01:30 / 04:55</text>
      <rect x="306" y="12" width="9" height="7" fill="none" stroke="#fff" stroke-width="1.3"/>
      <circle cx="332" cy="16" r="3.5" fill="none" stroke="#fff" stroke-width="2.2" stroke-dasharray="2 1.2"/>
    </svg>
  </div>
</div>

<div class="divider abs"></div>

<section class="testimonial abs">
  <h3 class="col-title">Client Testimonial</h3>
  <div class="client"><div class="avatar" role="img" aria-label="Client portrait"></div><div><b>Reed Talbot</b><small>Businessman</small></div></div>
  <blockquote class="quote">Mauris urnaei elit, mattis non urna acem, ullamcorper ipsum dolor vula putatem lorem.</blockquote>
</section>

<section class="news abs">
  <h3 class="col-title">Latest News</h3>
  <div class="news-item"><div class="thumb" role="img" aria-label="News photo of a couple" style="background:linear-gradient(#8a8f96,#3a3f48)"></div><p>Nunc purus orci, adipiscing non ipsum non, pellentesque fringilla sapien.<time>October 15, 2013</time></p></div>
  <div class="news-item"><div class="thumb" role="img" aria-label="News photo of a woman" style="background:linear-gradient(#d9d3cc,#7a5a45)"></div><p>Nunc purus orci, adipiscing non ipsum non, pellentesque fringilla sapien.<time>October 15, 2013</time></p></div>
  <div class="news-item"><div class="thumb" role="img" aria-label="News photo of a house" style="background:linear-gradient(#7aa6d8,#9a9a90 55%,#4f7a34)"></div><p>Nunc purus orci, adipiscing non ipsum non, pellentesque fringilla sapien.<time>October 15, 2013</time></p></div>
</section>

<section class="newsletter abs">
  <h3 class="col-title">Signup for our Newletter</h3>
  <input type="text" value="Enter Your Email *" aria-label="Email">
  <div class="check"><span class="box"><svg width="11" height="9" viewBox="0 0 11 9"><path d="M1 4.5l3 3 6-6" fill="none" stroke="#fff" stroke-width="1.8"/></svg></span>To get notified of specific auctions, auction types or locations</div>
  <div class="subscribe">SUBSCRIBE NOW</div>
</section>

<div class="partners abs" aria-label="Association memberships">
  <div class="badge abs" style="left:133px;width:96px;border-radius:40px 40px 8px 8px"></div>
  <div class="badge abs" style="left:304px;top:24px;width:76px;height:40px;border-radius:6px"></div>
  <div class="badge abs" style="left:458px;top:24px;width:100px;height:40px"></div>
  <div class="badge abs" style="left:645px;width:50px;height:57px;border-radius:4px"></div>
  <div class="badge abs" style="left:781px;top:18px;width:40px;height:40px"></div>
</div>

<footer class="site-footer abs">
  <div class="footer-brand abs"><span class="brand-mark"></span><span class="brand-name">Martin Vorne</span></div>
  <div class="fcol abs" style="left:290px"><h4>Navigation</h4><ul><li>Home</li><li>About</li><li>Services</li><li>Contact</li></ul></div>
  <div class="fcol abs" style="left:406px"><h4>Auctions</h4><ul><li class="on">Upcoming Auctions</li><li>Online Auctions</li><li>Past Auctions</li></ul></div>
  <div class="fcol contact abs" style="left:529px"><h4>Contact Us</h4><ul>
    <li><svg width="9" height="9" viewBox="0 0 24 24"><path d="M6.6 10.8a15 15 0 0 0 6.6 6.6l2.2-2.2c.3-.3.7-.4 1-.2 1.1.4 2.3.6 3.6.6.6 0 1 .4 1 1V20c0 .6-.4 1-1 1A17 17 0 0 1 3 4c0-.6.4-1 1-1h3.5c.6 0 1 .4 1 1 0 1.3.2 2.5.6 3.6.1.3 0 .7-.2 1z" fill="#888"/></svg>+1800-555-0199</li>
    <li><svg width="10" height="8" viewBox="0 0 10 8"><rect width="10" height="8" fill="#888"/><path d="M0 0l5 4 5-4" fill="none" stroke="#e4e4e4"/></svg>info@vorneauctions.example</li>
    <li><svg width="8" height="11" viewBox="0 0 8 11"><path d="M4 0a4 4 0 0 1 4 4c0 3-4 7-4 7S0 7 0 4a4 4 0 0 1 4-4z" fill="#888"/><circle cx="4" cy="4" r="1.5" fill="#e4e4e4"/></svg><span style="line-height:18px;margin-top:2px">Your Address, Your Country<br>Your Zip Code</span></li>
  </ul></div>
  <div class="fcol abs" style="left:687px"><h4>Social</h4></div>
  <div class="social footer-social abs"><span class="s1"></span><span class="s2"></span><span class="s3"></span><span class="s4"></span></div>
</footer>

<div class="bottom abs">
  <span class="copy abs">Copyright 2014 © Martin Vorne - All Rights Reserved</span>
  <span class="links abs">Site Map &nbsp;&nbsp;•&nbsp;&nbsp; Privacy Policy</span>
</div>

</body>
</html>
```